Employee I.D. Card - Badge

We need an employee I.D. card designed. Our employees are going to be wearing these. I would like to have it look nice. Something professional yet cool (not uptight if that makes sense).
Project Scope:
Vertical orientation
Company name ------------- (Bright and Tidy)
Website ------------- (brightandtidymn.example)
Employee Picture
background check image
front and back designed - same design on either side
You can create the card without having the employee images on them.
Here are the dimensions -
2.125 x 3.370 inches
Double sided - same design can be used front and back
Background badge - I would like to add an image that shows that the employee has taken a background check. I've added the press-kit for the company we use. If you have a better idea than incorporating their logo, we can certainly do something different.
Example image-
https://www.findwell-search.example/results?q=background+check+badge&mode=images
The print company will set up the names.
Logo is attached
Also attached are our business cards. You can use this for an idea of brand/company style.
Our website - brightandtidymn.example

```html
<!DOCTYPE html>
<html lang="en">
<head>
<meta charset="utf-8">
<title>Bright and Tidy – Employee ID Badge</title>
<link href="https://fonts.googleapis.com/css2?family=Arimo:wght@400&display=swap" rel="stylesheet">
<style>
  :root {
    --backdrop: #5b5b5d;
    --stripe-blue: #4ac7f2;
    --stripe-grey: #d1d3d4;
    --card-face: #e6e7e8;
    --ring-blue: #29abe2;
    --slot-grey: #9a9b9d;
    --ink: #111111;
    --brand-blue: #1b75bb;
    --url-grey: #58595b;
    --seal-gold: #d9a928;
    --seal-gold-light: #f3d77a;
    --seal-dark: #1f1f1f;
  }
  html, body {
    margin: 0;
    padding: 0;
    width: 1200px;
    height: 1200px;
    overflow: hidden;
    background: var(--backdrop);
  }
  .canvas {
    position: relative;
    width: 1200px;
    height: 1200px;
  }
  .badge-card {
    position: absolute;
    left: 259px;
    top: 60px;
    width: 681px;
    height: 1080px;
    font-family: "Arimo", Arial, sans-serif;
  }
  .badge-art {
    position: absolute;
    inset: 0;
    display: block;
  }
  .name-field {
    position: absolute;
    left: 0;
    right: 0;
    top: 164px;
    margin: 0;
    text-align: center;
    font-size: 38px;
    font-weight: 400;
    line-height: 1;
    color: var(--ink);
    letter-spacing: 0.5px;
  }
  .company-name {
    position: absolute;
    left: 54px;
    top: 800px;
    margin: 0;
    font-size: 62px;
    font-weight: 400;
    line-height: 1.02;
    color: var(--brand-blue);
    letter-spacing: -1px;
  }
  .company-url {
    position: absolute;
    left: 46px;
    top: 1024px;
    margin: 0;
    font-size: 23px;
    font-weight: 400;
    line-height: 1;
    color: var(--url-grey);
  }
</style>
</head>
<body>
<main class="canvas">
  <section class="badge-card" aria-label="Bright and Tidy employee ID badge">
    <svg class="badge-art" viewBox="0 0 634 1004" width="681" height="1080" aria-hidden="false">
      <defs>
        <linearGradient id="photoFill" x1="0" y1="0" x2="0" y2="1">
          <stop offset="0" stop-color="#e6e7e8"/>
          <stop offset="0.55" stop-color="#8fd3ef"/>
          <stop offset="1" stop-color="#29abe2"/>
        </linearGradient>
        <radialGradient id="sealFill" cx="0.4" cy="0.35" r="0.7">
          <stop offset="0" stop-color="var(--seal-gold-light)"/>
          <stop offset="1" stop-color="var(--seal-gold)"/>
        </radialGradient>
      </defs>

      <!-- card face -->
      <rect class="card-face" x="0" y="0" width="634" height="1004" fill="var(--card-face)"/>

      <!-- striped header band -->
      <g class="header-stripes">
        <rect x="0" y="0" width="634" height="580" fill="var(--stripe-grey)"/>
        <rect x="0" y="18" width="634" height="45" fill="var(--stripe-blue)"/>
        <rect x="0" y="101" width="634" height="45" fill="var(--stripe-blue)"/>
        <rect x="0" y="184" width="634" height="45" fill="var(--stripe-blue)"/>
        <rect x="0" y="268" width="634" height="45" fill="var(--stripe-blue)"/>
        <rect x="0" y="351" width="634" height="45" fill="var(--stripe-blue)"/>
        <rect x="0" y="434" width="634" height="45" fill="var(--stripe-blue)"/>
        <rect x="0" y="518" width="634" height="45" fill="var(--stripe-blue)"/>
      </g>

      <!-- lanyard slot -->
      <rect class="lanyard-slot" x="220" y="32" width="175" height="21" rx="10.5" fill="var(--slot-grey)"/>

      <!-- employee photo frame -->
      <circle class="photo-ring" cx="318" cy="450" r="232" fill="var(--card-face)" stroke="var(--ring-blue)" stroke-width="9"/>
      <circle class="photo-area" cx="318" cy="450" r="226" fill="url(#photoFill)" role="img" aria-label="Employee photo placeholder"/>

      <!-- background check seal -->
      <g class="check-seal" role="img" aria-label="Background check cleared seal">
        <circle cx="492" cy="627" r="92" fill="url(#sealFill)"/>
        <circle cx="492" cy="627" r="80" fill="var(--seal-dark)"/>
        <circle cx="492" cy="627" r="46" fill="url(#sealFill)"/>
      </g>
    </svg>

    <h2 class="name-field">NAME</h2>
    <h1 class="company-name">Bright and<br>Tidy</h1>
    <p class="company-url">www.brightandtidymn.example</p>
  </section>
</main>
</body>
</html>
```